GVA Business Card

I would like to create a busienss card for the high school teachers. Our school colors are red and black and our mascot is the bulldog. In addition, to our school address and contact information, I would like to add our twitter account and fb account. We also have a school website. Somewhere I would like to incorporate our school wide expectations: Be Safe, Be Respectful, Be Responsible and Be a Learner.

Tillbrook High School
2424 Fernwick
Tillbrook, KS 67193
785.904.2718
785.904.2719(fax)
www.tillbrookacademies.org
www.facebook.com/TillbrookHornets
twitter.com/TillbrookKsDST or @TillbrookKsDST
Teacher Name:
Teacher Email:

I would like to personalize each card with the teacher name and their email.

I would also like to use Hornet Circle – Roots.Now.Ahead

                                      Front Side of Card:  Teacher and School Contact Information

Back Side of Card:  Hornet Circle -several designers have asked about this-our school is trying to promote that we are a family trying to promote a positive climate.  We also want to add Roots.Now.Ahead with information that might pertain to the past, present, or future to keep people coming back to our website or facebook.

At first I mentioned that I wanted to use the bulldog as the graphic because it is our mascot, now I am changing my mind about maybe something more student centered like a group of stick figures circle together or arms around each other symbolizing that we are working together to accomplish our goal.

I need to make sure that our school wide expectations are also incorporated:

Be Safe.Be Respectful.Be Responsible.Be A Learner

Target Market(s)

9-12 students and professionals

Industry/Entity Type

High School

Requirements
Must have
• Contact information
Hornet Circle with Past, Present and Future Incorporated
Two sided business card
Side #1 Contact Info + graphic (might use bulldog that I attached however not sure if I like it)
Side #2 Hornet Circle with Past, Present and Future (incorporate a graphic that symbolizes togetherness or working together.

```html
<!DOCTYPE html>
<html lang="en">
<head>
<meta charset="utf-8">
<title>Tillbrook High School – Teacher Business Card</title>
<link rel="stylesheet" href="https://fonts.googleapis.com/css2?family=Mulish:wght@300;400&display=swap">
<style>
  :root {
    --paper: #ffffff;
    --ink: #231f20;
    --rule: #3a3a3a;
  }
  * { box-sizing: border-box; margin: 0; padding: 0; }
  html, body {
    width: 1017px;
    height: 1200px;
    overflow: hidden;
    background: var(--paper);
  }
  body {
    position: relative;
    font-family: "Mulish", "Helvetica Neue", Arial, sans-serif;
    font-weight: 300;
    color: var(--ink);
  }
  .card {
    position: absolute;
    left: 171px;
    width: 690px;
    height: 446px;
    border: 1.3px solid var(--ink);
    background: var(--paper);
  }
  .card--front { top: 102px; }
  .card--back  { top: 637px; }

  .rule {
    position: absolute;
    left: 67px;
    width: 552px;
    height: 0;
    border-top: 1.3px solid var(--rule);
  }

  .school-mark {
    position: absolute;
    left: 0;
    right: 0;
    top: 18px;
    height: 290px;
    display: flex;
    align-items: center;
    justify-content: center;
    font-size: 72px;
    font-weight: 300;
    letter-spacing: 4px;
    color: var(--ink);
  }

  .motto {
    position: absolute;
    left: 0;
    right: 0;
    top: 350px;
    text-align: center;
    font-size: 32px;
    line-height: 1;
    font-weight: 300;
  }

  .info-block {
    position: absolute;
    left: 0;
    right: 0;
    text-align: center;
    font-size: 23px;
    line-height: 28.7px;
    font-style: normal;
  }
  .teacher      { top: 17px; }
  .address      { top: 102px; }
  .contact      { top: 218px; }
  .expectations { top: 390px; font-size: 22.5px; }
</style>
</head>
<body>

  <section class="card card--front" aria-label="Card front">
    <p class="school-mark" aria-label="School mark">GVA</p>
    <div class="rule" style="top:331px"></div>
    <p class="motto">Roots. Now. Ahead.</p>
    <div class="rule" style="top:408px"></div>
  </section>

  <section class="card card--back" aria-label="Card back">
    <div class="info-block teacher">
      <p>Teacher Name:</p>
      <p>Teacher Email:</p>
    </div>
    <div class="rule" style="top:87px"></div>

    <address class="info-block address">
      <p>Tillbrook High School</p>
      <p>2424 Fernwick</p>
      <p>Tillbrook, KS 67193</p>
    </address>
    <div class="rule" style="top:204px"></div>

    <div class="info-block contact">
      <p>Phone us: 785.904.2718</p>
      <p>Or fax us: 785.904.2719</p>
      <p>www.tillbrookacademies.org</p>
      <p>www.facebook.com/TillbrookHornets</p>
      <p>@TillbrookKsDST</p>
    </div>
    <div class="rule" style="top:376px"></div>

    <p class="info-block expectations">Be Safe, Be Respectful, Be Responsible, and Be a Learner.</p>
  </section>

</body>
</html>
```